Modern Attractive Letterhead for Veterinary House Call Business.

A letterhead which can be printed on A4, A5 and A6 paper sizes.
To have: ( our files to be uploaded)
1. Logo with Text
2. telephone
3. email
4. website
5. Address

Target Market(s)

60-85year mainly women pet owners. Also market include families, young professionals, busy people who have dogs and cats

Industry/Entity Type

Business

Requirements
Must have
• 1. Logo with Text ( provided)
• 2. telephone
• 3. email
• 4. website
• 5. Address
Nice to have
• Needs to be modern, preferably warm and caring in nature( if possible )
Should not have
• difficulty in printing A5 and A6

```html
<!DOCTYPE html>
<html lang="en">
<head>
<meta charset="utf-8">
<title>Hearthside Vet Letterhead</title>
<link rel="stylesheet" href="https://fonts.googleapis.com/css2?family=Cinzel:wght@400;600&display=swap">
<style>
  :root {
    --backdrop: #e9e9e9;
    --paper: #ffffff;
    --brand-blue: #1f5fbf;
    --deep-blue: #1536a0;
    --sky-blue: #4ad0f5;
    --bar-blue: #1e8fdc;
    --leaf-green: #5cb82e;
    --ink: #1e1e2a;
    --rule: #b9b9c2;
  }
  html, body {
    margin: 0;
    padding: 0;
    width: 989px;
    height: 1200px;
    overflow: hidden;
    background: var(--backdrop);
  }
  .letterhead {
    position: absolute;
    left: 54px;
    top: 30px;
    width: 880px;
    height: 1140px;
    background: var(--paper);
    box-shadow: 0 2px 10px rgba(0,0,0,0.12);
    overflow: hidden;
    font-family: "Cinzel", "Times New Roman", serif;
  }
  .corner-block {
    position: absolute;
    left: 0;
    top: 0;
    width: 51px;
    height: 161px;
    background: linear-gradient(90deg, var(--deep-blue), var(--brand-blue) 70%, #3d8de0);
  }
  .corner-line {
    position: absolute;
    left: 53px;
    top: 0;
    width: 2px;
    height: 161px;
    background: var(--leaf-green);
  }
  .brand-disc {
    position: absolute;
    left: 14px;
    top: 42px;
    width: 108px;
    height: 108px;
    border-radius: 50%;
    background: var(--paper);
  }
  .brand-name {
    position: absolute;
    left: 136px;
    top: 78px;
    margin: 0;
    font-size: 32px;
    font-weight: 600;
    letter-spacing: 0.5px;
    color: var(--brand-blue);
    white-space: nowrap;
  }
  .contact-list {
    position: absolute;
    left: 563px;
    top: 45px;
    height: 110px;
    margin: 0;
    padding: 0 0 0 12px;
    list-style: none;
    border-left: 1px solid var(--rule);
  }
  .contact-item {
    display: flex;
    align-items: center;
    height: 31px;
    font-size: 17px;
    color: var(--ink);
    white-space: nowrap;
  }
  .contact-icon {
    width: 18px;
    height: 18px;
    margin-right: 8px;
    flex: none;
  }
  .side-bar {
    position: absolute;
    right: 0;
    top: 0;
    width: 5px;
    height: 134px;
    background: var(--bar-blue);
  }
  .footer-rule {
    position: absolute;
    left: 0;
    right: 0;
    top: 1086px;
    height: 2px;
    background: var(--leaf-green);
  }
  .footer-band {
    position: absolute;
    left: 0;
    right: 0;
    top: 1092px;
    height: 48px;
    background: linear-gradient(90deg, #2a86d6 0%, var(--sky-blue) 42%, #2f7fd6 75%, var(--deep-blue) 100%);
    display: flex;
    align-items: center;
  }
  .footer-address {
    margin: 0 0 0 170px;
    display: flex;
    align-items: center;
    font-size: 18px;
    color: #ffffff;
    letter-spacing: 0.3px;
    white-space: nowrap;
  }
  .home-icon {
    width: 18px;
    height: 18px;
    margin-right: 8px;
  }
</style>
</head>
<body>
  <main class="letterhead">
    <header class="letterhead-header">
      <div class="corner-block"></div>
      <div class="corner-line"></div>
      <div class="brand-disc"></div>
      <h1 class="brand-name">Hearthside Vet</h1>

      <ul class="contact-list">
        <li class="contact-item">
          <svg class="contact-icon" viewBox="0 0 18 18" aria-hidden="true">
            <circle cx="9" cy="9" r="8" fill="none" stroke="#2b7fd4" stroke-width="1.4"/>
            <path d="M6.2 4.6c.6-.4 1.2-.2 1.5.4l.6 1.3c.2.5 0 .9-.4 1.2l-.5.4c.4 1.1 1.2 2 2.3 2.6l.5-.5c.4-.4.9-.4 1.3-.1l1.1.8c.5.4.5 1 .1 1.5-.8.9-2 1.1-3.2.5C7.4 11.6 5.7 9.6 5.1 7.5c-.3-1.1.2-2.3 1.1-2.9z" fill="#2b7fd4"/>
          </svg>
          0491570110
        </li>
        <li class="contact-item">
          <svg class="contact-icon" viewBox="0 0 18 18" aria-hidden="true">
            <rect x="1.5" y="4" width="15" height="10" rx="1" fill="#2b6fd0"/>
            <path d="M1.8 4.5 9 10l7.2-5.5" fill="none" stroke="#ffffff" stroke-width="1.2"/>
          </svg>
          Info@hearthsidevet.com.au
        </li>
        <li class="contact-item">
          <svg class="contact-icon" viewBox="0 0 18 18" aria-hidden="true">
            <circle cx="9" cy="9" r="7.5" fill="#6fb3ee" stroke="#2b6fd0" stroke-width="1.2"/>
            <ellipse cx="9" cy="9" rx="3.2" ry="7.5" fill="none" stroke="#2b6fd0" stroke-width="1"/>
            <path d="M1.5 9h15M3 5h12M3 13h12" stroke="#2b6fd0" stroke-width="1"/>
          </svg>
          Www.hearthsidevet.com.au
        </li>
      </ul>
      <div class="side-bar"></div>
    </header>

    <footer class="letterhead-footer">
      <div class="footer-rule"></div>
      <div class="footer-band">
        <p class="footer-address">
          <svg class="home-icon" viewBox="0 0 18 18" aria-hidden="true">
            <path d="M9 2 1.5 8.5h2.2V16h4v-4.5h2.6V16h4V8.5h2.2z" fill="#ffffff"/>
          </svg>
          Po Box 2250 Wattlebrook Qld 4102
        </p>
      </div>
    </footer>
  </main>
</body>
</html>
```